Redesign This Psychology Website

We would like a slight redesign of this successful psychology (relationship counselling) website:

www.TheLumaHaven.com.au

We are updating the website, and we'd like a slight refresh of the design and style.

Please keep to very similar colours, and use the same logo. We're looking for around 10 page templates, however the main one is the home page.

Keep in mind, this website already converts quite well, so we want a new, fresh design in keeping with this one. Please don't bother designing something too extremely different.

thanks :)
Updates

Target Market(s)

couples who are looking for relationship counselling. Men and women, 25 - 70, across Australia

Industry/Entity Type

Psychology

Number of Pages Required

5+ page

Font styles to use
Sans Serif

Colors
87cfc6
b7a5cd
ec1f27
ffffff
cee9f5

Requirements
Must have
• a similar look to the current design, just looking for a slight refresh.
• Search bar
• Areas for lots of photos
• same logo
• lots of content areas
Nice to have
• great content areas, where we can display a lot of content and our areas.
Should not have
• no colors like orange, etc.
• should not have a totally different feel.

```html
<!DOCTYPE html>
<html lang="en">
<head>
<meta charset="utf-8">
<title>The Luma Haven – Relationship Counselling</title>
<link rel="stylesheet" href="https://fonts.googleapis.com/css2?family=PT+Sans:ital,wght@0,400;0,700;1,400;1,700&display=swap">
<style>
:root{
  --teal:#17848f;
  --teal-light:#4fb3bb;
  --teal-pale:#cfe9ec;
  --red:#e5202a;
  --ink:#333;
  --dark:#3b3b3b;
  --grey-band:#ececec;
  --white:#fff;
  --map:#d8d8d8;
  --panel:rgba(110,110,110,.92);
}
*{box-sizing:border-box;margin:0;padding:0}
html,body{width:1200px;height:2187px;overflow:hidden}
body{font-family:"PT Sans",Arial,sans-serif;color:var(--ink);background:var(--white);position:relative}
.abs{position:absolute}
a{color:inherit;text-decoration:none}

/* top bar */
.topbar{position:absolute;left:0;top:0;width:1200px;height:25px;background:var(--dark);color:#ddd;font-size:11px}
.topbar .cart{position:absolute;left:160px;top:5px;display:flex;align-items:center;gap:5px}
.topbar .cart .count{width:15px;height:15px;border-radius:50%;background:var(--teal-light);color:#fff;font-size:9px;display:flex;align-items:center;justify-content:center}
.topbar .links{position:absolute;right:160px;top:6px;display:flex;gap:20px;text-transform:uppercase;font-size:10.5px}
.topbar .links .hot{color:var(--red)}

/* header */
.header{position:absolute;left:0;top:25px;width:1200px;height:75px;background:linear-gradient(#fff,#f1f1f1)}
.brand{position:absolute;left:180px;top:12px;display:flex;align-items:center;gap:8px}
.brand .dot{width:38px;height:38px;border-radius:50%;background:var(--teal)}
.brand .name{font-size:30px;color:var(--teal);font-weight:400;line-height:1}
.brand .tag{position:absolute;left:46px;top:40px;font-size:11px;color:var(--teal);white-space:nowrap}
.search{position:absolute;left:893px;top:9px;width:150px;height:20px;border:1px solid #ddd;background:#fff;font-size:10px;font-style:italic;color:#aaa;padding:3px 6px}
.search svg{position:absolute;right:5px;top:4px}
.mainnav{position:absolute;right:163px;top:51px;display:flex;gap:15px;font-size:13.5px;color:var(--teal);text-transform:uppercase}
.mainnav .b{font-weight:700}

/* hero */
.hero{position:absolute;left:0;top:100px;width:1200px;height:524px;background:radial-gradient(ellipse at 45% 40%,#d6a38e 0,#b48060 18%,#6f9a3c 45%,#3f6f1f 80%)}
.callus{position:absolute;left:884px;top:388px;font-size:34px;font-weight:700;color:#fff;letter-spacing:.5px}
.phonebox{position:absolute;left:746px;top:423px;width:292px;height:55px;background:rgba(255,255,255,.9);color:var(--teal);font-size:42px;font-weight:700;text-align:center;line-height:55px}
.videobox{position:absolute;left:746px;top:512px;width:292px;height:54px;background:rgba(255,255,255,.9);padding:11px 0 0 28px;color:#333;line-height:1}
.videobox .s{font-size:11.5px;font-weight:700;text-transform:uppercase}
.videobox .l{font-size:18px;font-weight:700;text-transform:uppercase;margin-top:3px}
.videobox svg{position:absolute;right:30px;top:13px}

/* tabs */
.tabs{position:absolute;left:0;top:624px;width:1200px;height:88px;background:linear-gradient(#fff,#e9e9e9);border-bottom:2px solid var(--teal-pale)}
.tabs ul{list-style:none;position:absolute;left:157px;top:0;display:flex}
.tabs li{width:148px;height:88px;display:flex;align-items:center;justify-content:center;text-align:center;font-size:13px;font-weight:700;color:var(--teal);text-transform:uppercase;line-height:1.15;border-left:1px solid #d6d6d6}
.tabs li:first-child{border-left:0}
.tabs li.active{background:#fff;border-bottom:2px solid var(--teal-light)}

/* services */
.services{position:absolute;left:0;top:712px;width:1200px;height:378px}
.services .line{position:absolute;left:60px;top:182px;width:1080px;height:2px;background:linear-gradient(90deg,transparent,var(--teal-light) 10%,var(--teal-light) 90%,transparent)}
.svc{position:absolute;top:56px;width:220px;text-align:center}
.svc h3{font-size:15px;color:var(--red);text-transform:uppercase;line-height:1.2;height:40px}
.svc .photo{width:152px;height:152px;margin:10px auto 0;border-radius:50%;border:3px solid var(--teal-light);box-shadow:0 0 0 3px #fff inset}
.svc p{font-size:12px;margin-top:10px;line-height:1.25;color:#333;height:50px}
.svc .more{font-size:11px;color:var(--red);font-weight:700;display:block;margin-top:4px}

/* specialise */
.special{position:absolute;left:0;top:1090px;width:1200px;height:311px;background:var(--grey-band)}
.special h2{position:absolute;left:165px;top:32px;font-size:20px;color:var(--teal);text-transform:uppercase}
.special .copy{position:absolute;left:165px;top:70px;width:571px;font-size:12.5px;line-height:1.3;text-align:justify}
.special .copy p{margin-bottom:12px}
.finder{position:absolute;left:787px;top:32px;width:207px;text-align:center}
.finder h3{font-size:17px;color:var(--teal);text-transform:uppercase;line-height:1.2}
.finder .lbl{font-size:11px;font-style:italic;color:var(--teal);margin:14px 0 4px}
.field{height:24px;background:#fff;border:1px solid #ccc;font-size:11px;font-style:italic;color:#aaa;text-align:left;padding:5px 7px;position:relative}
.field svg{position:absolute;right:6px;top:8px}
.finder .or{font-size:11px;font-style:italic;color:#777;margin:4px 0}
.btn{display:inline-block;background:linear-gradient(#f44a50,var(--red));color:#fff;font-size:11px;font-weight:700;width:82px;height:22px;line-height:22px;border-radius:3px;text-transform:uppercase}

/* blog */
.blog{position:absolute;left:0;top:1401px;width:1200px;height:373px}
.blog h2{position:absolute;left:163px;top:40px;font-size:20px;color:var(--teal);text-transform:uppercase}
.blog .arrows{position:absolute;left:665px;top:45px}
.post{position:absolute;left:163px;width:545px}
.post .thumb{position:absolute;left:0;top:0;width:86px;height:86px;border-radius:50%;background:radial-gradient(circle,#e6d3c5,#9a8c82)}
.post .body{position:absolute;left:96px;top:0;width:444px}
.post h4{font-size:15px;font-style:italic;font-weight:400;color:var(--teal);text-transform:uppercase}
.post p{font-size:11.5px;font-style:italic;line-height:1.25;margin-top:5px}
.post .meta{display:flex;justify-content:space-between;margin-top:6px;font-size:11.5px;font-style:italic;color:var(--red)}
.post .meta b{font-style:normal;font-size:11px;padding-right:10px}
.topics{position:absolute;left:770px;top:72px;width:250px;height:255px}
.topics .q{position:absolute;font-size:10.5px;font-style:italic;font-weight:700;color:var(--teal);line-height:1.2}
.topics .l{right:135px;text-align:right}
.topics .r{left:132px}

/* map */
.mapband{position:absolute;left:0;top:1774px;width:1200px;height:365px;background:linear-gradient(120deg,#e2e2e2,#cfcfcf 50%,#dedede)}
.mapband .panel{position:absolute;left:744px;top:0;width:300px;height:365px;background:var(--panel);color:#fff;text-align:center}
.panel h3{font-size:15px;text-transform:uppercase;line-height:1.2;margin-top:44px}
.panel .field{width:200px;margin:20px auto 0}
.panel .cities{display:flex;justify-content:space-between;padding:0 18px;margin-top:14px;text-align:left;font-size:10.5px;line-height:1.22}
.panel .btn{margin-top:44px}

/* footer */
.footer{position:absolute;left:0;top:2139px;width:1200px;height:48px;background:var(--dark);color:#ddd;font-size:8px;border-bottom:6px solid var(--teal-light)}
.footer .left{position:absolute;left:163px;top:10px;line-height:1.5}
.footer .left .hot{color:var(--red)}
.footer .right{position:absolute;right:161px;top:10px;text-align:right;line-height:1.5;text-transform:uppercase}
</style>
</head>
<body>

<div class="topbar">
  <div class="cart">
    <svg width="16" height="14" viewBox="0 0 16 14" fill="none" stroke="#ddd" stroke-width="1.3"><path d="M1 1h2.5l2 8h8l1.5-5.5H4.5"/><circle cx="6.5" cy="12" r="1.2"/><circle cx="12.5" cy="12" r="1.2"/></svg>
    <span class="count">0</span><span>item(s) in shopping cart</span>
  </div>
  <nav class="links"><a class="hot">Join our associate program</a><a>Relationship counselling</a><a>Marriage counselling</a></nav>
</div>

<header class="header">
  <div class="brand"><span class="dot"></span><span class="name">The Luma Haven</span><span class="tag">helping you create loving relationships</span></div>
  <div class="search">Search
    <svg width="10" height="10" viewBox="0 0 10 10" fill="none" stroke="#999" stroke-width="1.3"><circle cx="4" cy="4" r="3"/><path d="M6.3 6.3L9 9"/></svg>
  </div>
  <nav class="mainnav"><a>Home</a><a>About</a><a>Resources</a><a>Blog</a><a>Shop</a><a class="b">Cart</a><a class="b">Search</a></nav>
</header>

<section class="hero" role="img" aria-label="Photo of a young couple lying in long green grass, foreheads touching">
  <div class="callus">CALL US</div>
  <div class="phonebox">1300 555 014</div>
  <div class="videobox">
    <div class="s">Who we are and what we do</div>
    <div class="l">Video presentation</div>
    <svg width="30" height="30" viewBox="0 0 30 30"><circle cx="15" cy="15" r="13" fill="none" stroke="#e5202a" stroke-width="2.5"/><path d="M12 9l9 6-9 6z" fill="#e5202a"/></svg>
  </div>
</section>

<nav class="tabs"><ul>
  <li>Councelling<br>types</li>
  <li class="active">Relationship<br>counselling<br>locations</li>
  <li>Sex therapy<br>locations</li>
  <li>Quizzes</li>
  <li>FAQ's</li>
  <li>Contact</li>
</ul></nav>

<section class="services">
  <div class="line"></div>
  <div class="svc" style="left:147px">
    <h3>Relationship<br>counselling</h3>
    <div class="photo" role="img" aria-label="Photo of a smiling couple" style="background:radial-gradient(circle,#eee,#c9c3bd)"></div>
    <p>Communication, Recovering from an affair, Loss of intimacy &amp; love, Power battles, Feeling like friends, not lovers</p>
    <a class="more">read more</a>
  </div>
  <div class="svc" style="left:370px">
    <h3>Sex therapy<br>counselling</h3>
    <div class="photo" role="img" aria-label="Photo of an older couple laughing in bed" style="background:radial-gradient(circle,#f4efe9,#d9c8b6)"></div>
    <p>Low libido , Erectile difficulties, Premature ejaculation, Differing libidos, Porn addiction, Keeping sex exciting</p>
    <a class="more">read more</a>
  </div>
  <div class="svc" style="left:594px">
    <h3>Anger management<br>counselling</h3>
    <div class="photo" role="img" aria-label="Photo of a frowning mature man" style="background:radial-gradient(circle,#f2f2f2,#c7c2bd)"></div>
    <p>Managing angry outbursts, expressing your anger in healthy ways</p>
    <a class="more">read more</a>
  </div>
  <div class="svc" style="left:820px">
    <h3>Narcissism<br>counselling</h3>
    <div class="photo" role="img" aria-label="Photo of a woman holding a yellow flower" style="background:radial-gradient(circle,#f3d7c5,#b0664a)"></div>
    <p>Managing narcissistic, superior, entitled, arrogant and lack of empathy tendencies in you or your partner</p>
    <a class="more">read more</a>
  </div>
</section>

<section class="special">
  <h2>We specialise in relationship &amp; marriage counselling</h2>
  <div class="copy">
    <p>At The Luma Haven, we are a group of PSYCHOLOGISTS, Australia wide who are passionate about relationships and helping you with yours.</p>
    <p>Our vision is to provide the most highly regarded and comprehensive marriage counselling and relationship counselling, and sex therapy in Australia, at reasonable and affordable rates.</p>
    <p>When we are experiencing relationship and marriage problems, there can be a lot of pain and confusion, and it can often be difficult to cope with the other areas of our lives when we are struggling with problems with our partner.</p>
    <p>We are not taught about relationships and how to have a good one in our schools, so most of us are doing the best we know how, but lack the knowledge on how to create a better relationship.</p>
  </div>
  <div class="finder">
    <h3>Find our psychologist<br>near you</h3>
    <div class="lbl">Type of Counselling</div>
    <div class="field">Please select<svg width="9" height="6" viewBox="0 0 9 6"><path d="M0 0h9L4.5 6z" fill="#999"/></svg></div>
    <div class="field" style="margin-top:12px">Location</div>
    <div class="or">OR</div>
    <div class="field">Postcode</div>
    <div style="margin-top:14px"><a class="btn">Search</a></div>
  </div>
</section>

<section class="blog">
  <h2>Latest articles from our blog</h2>
  <svg class="arrows" width="56" height="16" viewBox="0 0 56 16"><path d="M2 2h18l-9 13z" fill="#222"/><path d="M36 15h18l-9-13z" fill="#222"/></svg>

  <article class="post" style="top:106px">
    <div class="thumb" role="img" aria-label="Photo of a worried young woman"></div>
    <div class="body">
      <h4>What can I do if I'm living with a narcissist?</h4>
      <p>If you are in a relationship with a Narcissist, in his/her mind, you are an extension of him/her and he/she must always win, so his/her eruptions of temper and ego and devaluations and guilt are sharp and designed to cut you to the core, leaving you wounded.</p>
      <div class="meta"><span>February 24, 2017</span><b>read more</b></div>
    </div>
  </article>
  <article class="post" style="top:218px">
    <div class="thumb" role="img" aria-label="Photo of a young woman looking unsure"></div>
    <div class="body">
      <h4>Why am I with a narcissist?</h4>
      <p>You may be wondering why anyone would be masochistic enough to ever get themselves into a relationship with someone who has so many characteristics of a Narcissist and who leaves you feeling so dreadful?</p>
      <div class="meta"><span>February 22, 2017</span><b>read more</b></div>
    </div>
  </article>

  <div class="topics">
    <svg class="abs" style="left:0;top:0" width="250" height="255" viewBox="0 0 250 255">
      <defs><linearGradient id="hfade" x1="0" x2="1"><stop offset="0" stop-color="#4fb3bb" stop-opacity="0"/><stop offset=".5" stop-color="#4fb3bb"/><stop offset="1" stop-color="#4fb3bb" stop-opacity="0"/></linearGradient>
      <linearGradient id="vfade" x1="0" y1="0" x2="0" y2="1"><stop offset="0" stop-color="#4fb3bb" stop-opacity="0"/><stop offset=".5" stop-color="#4fb3bb"/><stop offset="1" stop-color="#4fb3bb" stop-opacity="0"/></linearGradient></defs>
      <rect x="123" y="0" width="2" height="255" fill="url(#vfade)"/>
      <rect x="0" y="100" width="250" height="1.5" fill="url(#hfade)"/>
      <rect x="0" y="164" width="250" height="1.5" fill="url(#hfade)"/>
      <rect x="0" y="36" width="250" height="1.5" fill="url(#hfade)"/>
      <rect x="0" y="226" width="250" height="1.5" fill="url(#hfade)"/>
    </svg>
    <div class="q l" style="top:63px">How to deal<br>with an affair?</div>
    <div class="q r" style="top:63px">Is one of you an<br>Intimacy Withholder?</div>
    <div class="q l" style="top:123px">Some Sex<br>Relationships</div>
    <div class="q r" style="top:123px">Is too much porn<br>affecting your relationship?</div>
    <div class="q l" style="top:185px">Are you living<br>with a narcissist?</div>
    <div class="q r" style="top:185px">Is your relationship safe?<br>Is your partner controlling?</div>
  </div>
</section>

<section class="mapband" role="img" aria-label="Grey road map of the region showing towns and highways">
  <div class="panel">
    <h3>Our relationship counselling<br>locations across Australia</h3>
    <div class="field">Please select city<svg width="9" height="6" viewBox="0 0 9 6"><path d="M0 0h9L4.5 6z" fill="#999"/></svg></div>
    <div class="cities">
      <div>Sydney – 13 centres<br>Canberra – 2 centres<br>Melbourne – 21 centres<br>Perth – 12 centres<br>Brisbane – 14 centres<br>Wollongong – 1 centre<br>Central Coast – 2 centres</div>
      <div>Adelaide – 4 centres<br>Gold Coast – 5 centres<br>Sunshine Coast – 2 centres<br>Cairns – 1 centre<br>Townsville – 1 centre<br>Wodonga – 1 centre</div>
    </div>
    <a class="btn">Search</a>
  </div>
</section>

<footer class="footer">
  <div class="left">© Copyright The Luma Haven 2017 &nbsp; <span class="hot">Find us on social</span><br>Privacy Policy / Terms &amp; Conditions / Site Map / Associate Psychologists / Program / Contact Us</div>
  <div class="right">The Luma Haven<br>Call us on 1300 555 014</div>
</footer>

</body>
</html>
```